Product sheet for managing talented people!

We need a new product sheet to describe our method of helping organisations to manage their talented people! We have selected a rowing team as the graphical theme (sample attached - please select or suggest a new picture if you want). We have also attached a powerpoint slide with our model (this is the service we offer).

FRONT PAGE

We are looking for an eye-catching front page that uses our 1. "Kestrel Growth Model"; 2. a picture of a rowing team of 8, and 3. our logo and 1800 KESTRL phone number (1800 537 875).

Step 1 - Assess key positions to determine your Talent Management Priorities.

Step 2 - Organisational psychology support helps individuals self-evaluate (see page 2 for details).

Step 3 - Facilitate agreement with manager and embed best-practice in organisational fairness.

Step 4 - Tailor career development and redeployment options based on shared understanding.

Step 5 - Evaluate ROI for individual performance and engagement.

BACK PAGE

The second page will have more detail of each of the talent categories also included in the powerpoint slide. Logo attached also. Please also view our website as the graphics should give you a sense of the look and feel of our brand - www.kestrelgm.com.au We have also added another flyer that we still use - please do not reverse the logo on this project - use in current form. CORPORATE LOGO / COLOUR GUIDE
C100 M50 Y0 K0
C100 M50 Y0 K0
C100 M50 Y0 K0
Gradient
C100 M60 Y0 K40
C100 M45 Y0 K0
C100 M20 Y0 K0
C70 M0 Y0 K0
PMS 2935 C
PMS 2935 C 75% Tint
PMS 2935 C
PMS Process Cyan C

The successful flyer will need to be print ready (as per attached example) and in pdf form so that we can print and/or send as a PDF.

Thanks.

Target Market(s)

Human Resource Managers in business and government.

Industry/Entity Type

Product

Requirements
Must have
• Eye-catching graphics with a rowing team theme. Colours consistent with our corporate colour codes.
Nice to have
• Please add small "trademark" symbol to the logo. This is small TM in a circle and usually placed at top right hand of logo. PLease add our website address www.kestrelgm.com
Should not have
• Please do not "reverse" the logo - use as is.

```html
<!DOCTYPE html>
<html lang="en">
<head>
<meta charset="utf-8">
<title>Kestrel Growth Management – Product Sheet</title>
<link href="https://fonts.googleapis.com/css2?family=Tinos:ital,wght@0,400;0,700;1,400&family=PT+Sans:ital,wght@0,400;1,400&display=swap" rel="stylesheet">
<style>
:root{
  --navy:#1d3d8c;
  --blue:#2a57b5;
  --logo-blue:#2f4b9f;
  --ink:#231f20;
  --accent:#9bbcff;
  --white:#ffffff;
  --paper:#f2f2f2;
  --serif:'Tinos', 'Times New Roman', serif;
  --sans:'PT Sans', Arial, sans-serif;
}
*{margin:0;padding:0;box-sizing:border-box}
html,body{width:1200px;height:1200px;overflow:hidden;background:#e9e9e9}
.canvas{position:relative;width:1200px;height:1200px}
.page{position:absolute;top:207px;width:527px;height:740px;transform:scale(1.0626);transform-origin:top left;overflow:hidden;box-shadow:0 4px 14px rgba(0,0,0,.25)}
.page--front{left:30px;background:var(--ink)}
.page--back{left:610px;background:var(--white)}
.page svg.shapes{position:absolute;inset:0;width:527px;height:740px}
.abs{position:absolute}

/* brand name */
.brand{font-family:var(--serif);color:var(--logo-blue);font-weight:400;text-align:center}
.brand__name{font-size:44px;letter-spacing:1px;line-height:1}
.brand__sub{font-size:9.5px;letter-spacing:2.6px;margin-top:4px}

/* front */
.front-headline{left:30px;top:220px;font-family:var(--serif);font-weight:700;color:var(--white);font-size:14.5px;line-height:1;letter-spacing:.2px}
.front-headline span{display:block;font-size:11.5px;margin-top:1px}
.step{left:0;width:275px;font-family:var(--serif);font-weight:700;color:var(--white);font-size:10.2px;line-height:17px}
.step__num{position:absolute;left:0;top:0;width:30px;height:18px;background:var(--white);color:var(--navy);font-size:19px;line-height:18px;text-align:center;clip-path:polygon(0 0,100% 0,82% 100%,0 100%)}
.step__text{margin-left:37px;display:block}
.step__note{margin:4px 10px 0 37px;font-family:var(--sans);font-style:italic;font-weight:400;font-size:7.2px;line-height:10px}
.contact-box{left:20px;top:555px;width:267px;height:135px;background:linear-gradient(#ffffff,#e9e9e9);border-radius:10px 10px 0 0;padding:18px 10px 0 11px;font-family:var(--serif)}
.contact-box p{font-size:11px;line-height:16.5px;color:var(--ink)}
.contact-box strong{display:block;margin-top:12px;font-weight:400;font-size:13.5px;line-height:16px;color:var(--blue)}
.front-web{left:32px;top:700px;font-family:var(--sans);color:var(--white);font-size:13px;letter-spacing:2.4px}
.photo-frame{border:3px solid var(--white);border-radius:9px;overflow:hidden;box-shadow:0 2px 6px rgba(0,0,0,.4)}
.photo-frame div{width:100%;height:100%}
.process-pill{left:313px;top:161px;width:171px;height:27px;border-radius:8px;background:linear-gradient(#ffffff,#dcdcdc);font-family:var(--serif);font-weight:700;color:var(--blue);font-size:22px;line-height:27px;text-align:center}
.process-list{font-family:var(--sans);color:var(--white);font-size:11.2px;line-height:17px;list-style:none}
.process-list li{padding-bottom:5px;margin-bottom:2px;border-bottom:1px solid rgba(255,255,255,.12)}
.process-list em{color:var(--accent)}
.process-list--front{left:313px;top:200px;width:200px}

/* back */
.back-quote{left:300px;top:300px;width:227px;text-align:center;font-family:var(--serif);font-weight:700;color:var(--white);font-size:12px;line-height:20px;letter-spacing:.5px}
.process-list--back{left:305px;top:452px;width:222px;text-align:center}
.traits{left:17px;width:290px;font-family:var(--serif);color:var(--white)}
.traits h3{font-size:11.5px;font-weight:700;margin-bottom:7px}
.traits__cols{display:flex}
.traits ul{list-style:none;font-size:7.8px;line-height:10.5px}
.traits ul:first-child{width:145px;padding-left:0}
.traits li{position:relative;padding-left:10px;margin-bottom:3px}
.traits li::before{content:"";position:absolute;left:1px;top:3.5px;width:4px;height:4px;border-radius:50%;background:var(--white)}
.back-footer{left:0;top:700px;width:527px;height:40px;font-family:var(--serif);font-weight:700;font-size:12px;color:var(--ink);text-align:center;line-height:38px}
</style>
</head>
<body>
<main class="canvas">

  <!-- FRONT PAGE -->
  <section class="page page--front">
    <svg class="shapes" viewBox="0 0 527 740" aria-hidden="true">
      <defs>
        <linearGradient id="frontPaper" x1="0" y1="0" x2="1" y2="0.3">
          <stop offset="0" stop-color="#ffffff"/><stop offset="1" stop-color="#e4e4e4"/>
        </linearGradient>
        <linearGradient id="frontBlue" x1="0" y1="0" x2="1" y2="1">
          <stop offset="0" stop-color="#1c3c8a"/><stop offset="1" stop-color="#234aa0"/>
        </linearGradient>
      </defs>
      <rect x="0" y="0" width="275" height="230" fill="url(#frontPaper)"/>
      <path d="M0,197 C100,182 200,168 275,164 L275,520 C287,600 322,660 370,690 L0,690 Z" fill="url(#frontBlue)"/>
      <path d="M275,500 C282,590 320,655 385,690 L362,690 C312,656 282,600 275,520 Z" fill="#ffffff"/>
    </svg>

    <div class="abs brand" style="left:45px;top:95px;width:190px">
      <div class="brand__name">KESTREL</div>
      <div class="brand__sub">GROWTH MANAGEMENT</div>
    </div>

    <h1 class="abs front-headline">EXECUTIVE COACHING AND<span>CAREER DEVELOPMENT EXPERTS</span></h1>

    <div class="abs step" style="top:268px">
      <span class="step__num">1</span>
      <span class="step__text">Assess key positions to determine your Talent Management Priorities.</span>
      <p class="step__note">Offers several levels of career transition support allowing you to select the program features that you believe are right for your departing employee. These program options are detailed below, and can be modified to suit your needs. All programs include reporting on client progress and outcomes.</p>
    </div>
    <div class="abs step" style="top:370px">
      <span class="step__num">2</span>
      <span class="step__text">Organisational psychology support helps individuals self-evaluate</span>
    </div>
    <div class="abs step" style="top:411px">
      <span class="step__num">3</span>
      <span class="step__text">Facilitate agreement with manager an embed best-practice in organisational fairness.</span>
    </div>
    <div class="abs step" style="top:455px">
      <span class="step__num">4</span>
      <span class="step__text">Tailor career development and redeployment options based on shared understanding.</span>
    </div>
    <div class="abs step" style="top:496px">
      <span class="step__num">5</span>
      <span class="step__text">Evaluate ROI for individual performance and engagement.</span>
    </div>

    <div class="abs contact-box">
      <p>Kestrel has first class offices in all capital cities and can provide on-site consultations with your key people by arrangement.</p>
      <strong>For a confidential discussion or advice 1800 KESTRL (1800 537 875)</strong>
    </div>

    <div class="abs front-web">www.kestrelgm.com.au</div>

    <div class="abs photo-frame" style="left:295px;top:25px;width:218px;height:110px">
      <div role="img" aria-label="Close-up photo of a rowing crew in red, white and blue pulling oars over a yellow boat" style="background:linear-gradient(160deg,#c83a3a 0%,#3b5fb0 35%,#e6e2d0 60%,#d9c34a 100%)"></div>
    </div>

    <div class="abs process-pill">A fair process</div>
    <ul class="abs process-list process-list--front">
      <li><em>Exit</em> – planned or managed</li>
      <li><em>Developing</em> - high risk/high reward</li>
      <li><em>Contributing</em> - probable flight risk</li>
      <li><em>Emerging</em> – manage career aspirations</li>
      <li><em>Elite</em> – mission critical or<br>market-sensitive</li>
      <li><em>Target</em> – strategic external hire<br>with market implications</li>
    </ul>

    <div class="abs photo-frame" style="left:333px;top:438px;width:160px;height:278px">
      <div role="img" aria-label="Aerial photo of an eight-person rowing crew on blue water" style="background:linear-gradient(180deg,#5d7f9e 0%,#3f6283 50%,#6b8aa6 100%)"></div>
    </div>
  </section>

  <!-- BACK PAGE -->
  <section class="page page--back">
    <svg class="shapes" viewBox="0 0 527 740" aria-hidden="true">
      <defs>
        <linearGradient id="backBlue" x1="0" y1="0" x2="1" y2="1">
          <stop offset="0" stop-color="#1c3c8a"/><stop offset="1" stop-color="#2b5cc0"/>
        </linearGradient>
      </defs>
      <path d="M0,255 C150,290 250,282 318,272 C300,420 335,560 360,700 L0,700 Z" fill="url(#backBlue)"/>
      <path d="M318,272 C390,258 460,240 527,212 L527,700 L360,700 C335,560 300,420 318,272 Z" fill="var(--ink)"/>
    </svg>
    <svg class="shapes" viewBox="0 0 527 740" role="img" aria-label="Photo of a rowing crew in navy kit with caps and sunglasses pulling oars">
      <defs>
        <linearGradient id="backPhoto" x1="0" y1="0" x2="1" y2="0.4">
          <stop offset="0" stop-color="#e8ecf2"/><stop offset="0.35" stop-color="#9fb0c9"/>
          <stop offset="0.65" stop-color="#34467a"/><stop offset="1" stop-color="#c9d3e0"/>
        </linearGradient>
      </defs>
      <path d="M0,130 C120,135 300,40 527,52 L527,205 C400,238 220,290 0,240 Z" fill="url(#backPhoto)"/>
    </svg>

    <div class="abs brand" style="left:25px;top:70px;width:150px">
      <div class="brand__name" style="font-size:34px">KESTREL</div>
      <div class="brand__sub" style="font-size:7.5px;letter-spacing:2px">GROWTH MANAGEMENT</div>
    </div>

    <div class="abs traits" style="top:290px">
      <h3>Characteristics – Exit</h3>
      <div class="traits__cols">
        <ul><li>Company or employee-initiated</li><li>May be disengaged/disgruntled</li><li>Poor hire</li></ul>
        <ul><li>Unforeseen circumstances</li><li>Better opportunity</li><li>Conflict</li></ul>
      </div>
    </div>
    <div class="abs traits" style="top:368px">
      <h3>Characteristics – Developing</h3>
      <div class="traits__cols">
        <ul><li>New talent</li><li>Needs to integrate external experience</li><li>Project-dependent*</li></ul>
        <ul style="margin-top:4px"><li>Growing industry connections</li><li>Personal brand aligned</li><li>with the business</li></ul>
      </div>
    </div>
    <div class="abs traits" style="top:451px">
      <h3>Characteristics – Contributing</h3>
      <div class="traits__cols">
        <ul><li>Transactional</li><li>Track record of quantifiable results</li><li>Commercial</li></ul>
        <ul><li>Stable</li><li>In the zone &amp; contributing today</li><li>Potential</li></ul>
      </div>
    </div>
    <div class="abs traits" style="top:533px">
      <h3>Characteristics – Emerging</h3>
      <div class="traits__cols">
        <ul><li>Engaged</li><li>Transformational</li><li>Strong personal brand</li></ul>
        <ul><li>Results multiplier who facilitates other's success</li><li>Promote 1 or 2 levels up</li></ul>
      </div>
    </div>
    <div class="abs traits" style="top:607px">
      <h3>Characteristics – Elite</h3>
      <div class="traits__cols">
        <ul><li>Executive presence</li><li>Established with strong external reputation</li><li>Potential successor to CEO</li></ul>
        <ul><li>Mature</li><li>Complex issues</li><li>Head-hunt risk</li></ul>
      </div>
    </div>

    <p class="abs back-quote">"TALENT ASSESSMENT"<br>AND<br>"HELP YOUR PEOPLE FIND<br>THEIR PERFECT ROLE AND<br>DEVELOP THEIR SKILLS<br>IN A FAIR PROCESS"</p>

    <ul class="abs process-list process-list--back">
      <li><em>Exit</em> – planned or managed</li>
      <li><em>Developing</em> - high risk/high reward</li>
      <li><em>Contributing</em> - probable flight risk</li>
      <li><em>Emerging</em> – manage career aspirations</li>
      <li><em>Elite</em> – mission critical or<br>market-sensitive</li>
      <li><em>Target</em> – strategic external hire<br>with market implications</li>
    </ul>

    <div class="abs back-footer">Call: 1800 KESTRL (1800 537 875) &nbsp;&nbsp;| &nbsp;&nbsp;Website: www.kestrelgm.com.au</div>
  </section>

</main>
</body>
</html>
```